Business card design needed

Name of Restaurant:
Olive and Ember
The Restaurant with a Difference

Target Market(s)

Food lovers, families

Industry/Entity Type

Business

Contact Information for Business Card

Mountains, sun rays

Logo Text

Olive and Ember The Restaurant with a difference

Logo styles of interest
Pictorial/Combination Logo
Abstract Logo
Requirements
Must have
• Mountains
Nice to have
• Sun rays

```html
<!DOCTYPE html>
<html lang="en">
<head>
<meta charset="utf-8">
<title>Olive and Ember – Business Card</title>
<link href="https://fonts.googleapis.com/css2?family=Open+Sans:wght@400;600&family=Sofia&display=swap" rel="stylesheet">
<style>
  :root {
    --page: #e9ebed;
    --card-edge: #ffffff;
    --card-blue: #2fa3dd;
    --deep-blue: #3a6f95;
    --pale-blue: #dff1fb;
    --text-light: #ffffff;
  }
  html, body {
    margin: 0;
    padding: 0;
    width: 1200px;
    height: 801px;
    overflow: hidden;
    background: var(--page);
  }
  .card {
    position: absolute;
    left: 430px;
    top: 40px;
    width: 340px;
    height: 720px;
  }
  .card-shape {
    position: absolute;
    inset: 0;
    width: 340px;
    height: 720px;
  }
  .brand {
    position: absolute;
    left: 0;
    top: 78px;
    width: 340px;
    text-align: center;
    color: var(--text-light);
    font-family: "Open Sans", sans-serif;
  }
  .brand-dot {
    display: block;
    width: 132px;
    height: 132px;
    margin: 0 auto 26px;
    border-radius: 50%;
    background: var(--deep-blue);
  }
  .brand-name {
    margin: 0;
    font-size: 37px;
    font-weight: 600;
    line-height: 1.15;
  }
  .brand-tagline {
    margin: 14px 0 0;
    font-size: 19px;
    font-weight: 400;
    line-height: 1.3;
    color: var(--pale-blue);
  }
  .holder-name {
    position: absolute;
    left: 0;
    top: 408px;
    width: 340px;
    margin: 0;
    text-align: center;
    font-family: "Sofia", cursive;
    font-size: 42px;
    font-weight: 400;
    line-height: 1.2;
    color: var(--text-light);
  }
  .contact {
    position: absolute;
    left: 0;
    top: 482px;
    width: 340px;
    margin: 0;
    padding: 0;
    list-style: none;
    text-align: center;
    font-family: "Open Sans", sans-serif;
    font-size: 20px;
    line-height: 29px;
    color: var(--text-light);
  }
</style>
</head>
<body>
  <div class="card">
    <svg class="card-shape" viewBox="0 0 340 720" xmlns="http://www.w3.org/2000/svg">
      <defs>
        <linearGradient id="mountainMist" x1="0" y1="0" x2="0" y2="1">
          <stop offset="0" stop-color="#2fa3dd" stop-opacity="0"/>
          <stop offset="0.5" stop-color="#6cc0ea" stop-opacity="0.7"/>
          <stop offset="1" stop-color="#4fb2e4" stop-opacity="0.5"/>
        </linearGradient>
      </defs>
      <polygon class="card-border" points="0,0 340,0 340,720 170,660 0,720" fill="var(--card-edge)"/>
      <polygon class="card-ribbon" points="12,12 328,12 328,700 170,646 12,700" fill="var(--card-blue)"/>
      <polygon class="mountain-backdrop" role="img" aria-label="Faint mountain range scenery"
               points="12,540 328,540 328,700 170,646 12,700" fill="url(#mountainMist)"/>
    </svg>

    <div class="brand">
      <span class="brand-dot"></span>
      <p class="brand-name">Olive and Ember</p>
      <p class="brand-tagline">The Restaurant with<br>a Difference</p>
    </div>

    <h1 class="holder-name">Your Name</h1>

    <ul class="contact">
      <li>phone: +000 000 000</li>
      <li>mobile: +000 000 000</li>
      <li>www.oliveandember.com</li>
      <li>office@oliveandember.com</li>
    </ul>
  </div>
</body>
</html>
```